'Wedding Business" Business Card Design

dj services for weddings and parties, uplighting, event planning, day of coordination for weddings, photography for weddings and other events.

Would like raised print and metallic also if possible. Elegant design, yet modern. This is a wedding business and should describe our goals and main services - DJ/lighting, wedding and event planning, photography. slogan "Simply Incredible, Incredibly simple" or "Your Dreams. Our Experience. The Perfect Match" Our goal is to provide multiple services to make it easier for the bride and groom almost like a one stop shop. Feel free to use the slogan or leave it out , we just want to really stand out against the competition. You can also get more info on our website www.brightlanestudios.com - we are working to get the brightlanenc.com site pointed to our current site!

there should be 2 files attached, if they did not go through please email events@brightlanenc.com or brightlanestudios@mailbox.test
Updates

Thank you all for your help, we have decided what we like but would like to make some changes, we need to order these asap so please let us know if you can help.

Reason: Wasn't able to pick it out in time! So Sorry but we know what we want!!

Industry/Entity Type

Business

Contact Information for Business Card

Marcus and Leona Whitcombe
555-318-2047
555-720-4861
Bright Lane Studios, Events, & Photography
EMAIL:Events@BrightLaneNC.com
www.brightlanenc.com

```html
<!DOCTYPE html>
<html lang="en">
<head>
<meta charset="utf-8">
<title>Bright Lane Studios – Business Card</title>
<link href="https://fonts.googleapis.com/css2?family=Arimo:wght@400;700&display=swap" rel="stylesheet">
<style>
  :root {
    --backdrop: #e6e4e0;
    --card-black: #0b0b0c;
    --card-sheen: #1c1c1f;
    --text-white: #f4f4f4;
    --text-grey: #c8c8cc;
    --silver: #c9cbd3;
    --hours-green: #3fcf4a;
    --band-blue: #4b4fcf;
  }
  * { margin: 0; padding: 0; box-sizing: border-box; }
  html, body { width: 1200px; height: 858px; overflow: hidden; }
  body {
    background: var(--backdrop);
    font-family: "Arimo", Arial, sans-serif;
    position: relative;
  }
  .card {
    position: absolute;
    background: linear-gradient(160deg, var(--card-sheen) 0%, var(--card-black) 45%, var(--card-black) 100%);
    box-shadow: 0 10px 28px rgba(0,0,0,0.28);
    color: var(--text-white);
    overflow: hidden;
  }
  .card-front {
    left: 60px; top: 269px; width: 560px; height: 320px;
    display: flex; flex-direction: column; justify-content: center; align-items: center;
  }
  .front-title {
    font-size: 38px; font-weight: 400; line-height: 1.3; text-align: center; letter-spacing: 0.3px;
  }
  .card-back {
    left: 780px; top: 149px; width: 330px; height: 560px;
    display: flex; flex-direction: column; align-items: center; text-align: center;
  }
  .brand-name {
    margin-top: 92px;
    font-size: 40px; font-weight: 400; color: var(--silver); letter-spacing: 1px;
  }
  .owners { margin-top: 58px; }
  .owner-names { font-size: 20px; font-weight: 700; }
  .owner-role { font-size: 16px; color: var(--text-grey); margin-top: 2px; }
  .hours { margin-top: 44px; font-size: 15px; color: var(--hours-green); }
  .contact { margin-top: 34px; font-size: 15px; line-height: 1.45; }
  .phone-line { display: flex; align-items: center; justify-content: center; gap: 8px; }
  .phone-icon { width: 13px; height: 13px; fill: var(--hours-green); }
  .web-band {
    position: absolute; left: 0; right: 0; bottom: 0; height: 62px;
    background: var(--band-blue);
    display: flex; align-items: center; justify-content: center;
    font-size: 24px; color: var(--text-white); letter-spacing: 0.5px;
  }
</style>
</head>
<body>
  <section class="card card-front">
    <h1 class="front-title">Bright Lane Studios<br>Events, &amp; Photography</h1>
  </section>

  <section class="card card-back">
    <div class="brand-name">Bright Lane</div>
    <div class="owners">
      <div class="owner-names">Marcus and Leona Whitcombe</div>
      <div class="owner-role">Owners</div>
    </div>
    <div class="hours">Sunday - Saturday 9:00am - 10:00pm</div>
    <div class="contact">
      <div class="phone-line">
        <svg class="phone-icon" viewBox="0 0 24 24" aria-hidden="true"><path d="M6.6 10.8a15.1 15.1 0 0 0 6.6 6.6l2.2-2.2a1 1 0 0 1 1-.25 11.4 11.4 0 0 0 3.6.57 1 1 0 0 1 1 1V20a1 1 0 0 1-1 1A17 17 0 0 1 3 4a1 1 0 0 1 1-1h3.5a1 1 0 0 1 1 1c0 1.25.2 2.45.57 3.57a1 1 0 0 1-.25 1z"/></svg>
        <span>555-720-4861</span>
      </div>
      <div class="phone-line">
        <svg class="phone-icon" viewBox="0 0 24 24" aria-hidden="true"><path d="M6.6 10.8a15.1 15.1 0 0 0 6.6 6.6l2.2-2.2a1 1 0 0 1 1-.25 11.4 11.4 0 0 0 3.6.57 1 1 0 0 1 1 1V20a1 1 0 0 1-1 1A17 17 0 0 1 3 4a1 1 0 0 1 1-1h3.5a1 1 0 0 1 1 1c0 1.25.2 2.45.57 3.57a1 1 0 0 1-.25 1z"/></svg>
        <span>555-318-2047</span>
      </div>
      <div>Events@BrightLaneNC.com</div>
      <div>42 maple hollow lane raleigh, nc 27601</div>
    </div>
    <div class="web-band">www.brightlanenc.com</div>
  </section>
</body>
</html>
```